Business Card Admin Services

I have just selected a new logo. Now I need a business card.

The business is contract administrative services. We provide high value administrative services to small businesses/offices. We are professional, efficient, but also have fun and energetic personalities.

Olive Parker
Olive@OfficeFalcon.ca
604-319-4870
OfficeFalcon.ca

I will also want Facely, Chirper and Linkup icons on the card - please up my "handles" beside each.
Facely is OfficeFalconCanada
Chirper is @OFalconOlive
Linkup is OliveParkerOfficeFalcon
Updates

New logo just updated.  Thanks for your patience!

Target Market(s)

Small businesses, professional offices

Industry/Entity Type

Business

Requirements
Must have
• bold, fun use of my colours
font needs to be consistent with the logo
Nice to have
• I quite like a closeup of the head

```html
<!DOCTYPE html>
<html lang="en">
<head>
<meta charset="utf-8">
<title>Office Falcon – Contract Administrative Services</title>
<link rel="stylesheet" href="https://fonts.googleapis.com/css2?family=Raleway:wght@400;700;800&display=swap">
<style>
  :root {
    --paper: #fdf3f5;
    --paper-edge: #f9dde3;
    --rose: #e8405f;
    --rose-soft: #f06c86;
    --rose-pale: #f5a8b8;
    --magenta: #d4317a;
    --wine: #a8223c;
    --ink: #3a3a3a;
    --rule: #d9c9cc;
    --white: #ffffff;
    --ring: #e9e4e5;
  }
  * { box-sizing: border-box; margin: 0; padding: 0; }
  html, body { width: 1200px; height: 687px; overflow: hidden; background: var(--white); }
  .card {
    position: relative;
    width: 1200px;
    height: 687px;
    overflow: hidden;
    background: radial-gradient(ellipse at 50% 45%, var(--white) 0%, var(--paper) 60%, var(--paper-edge) 100%);
    font-family: "Raleway", Arial, sans-serif;
  }
  .curtain { position: absolute; top: 0; height: 687px; width: 90px; }
  .curtain--left { left: 0; }
  .curtain--right { right: 0; }

  .badge { position: absolute; width: 309px; height: 82px; }
  .badge svg { position: absolute; inset: 0; }
  .badge__label {
    position: absolute;
    left: 34px; right: 34px; top: 0; height: 68px;
    display: flex; align-items: center; justify-content: center;
    color: var(--white);
    font-weight: 700;
    font-size: 23px;
    letter-spacing: 1px;
    white-space: nowrap;
  }
  .badge--quality { left: 91px; top: 71px; }
  .badge--professional { left: 91px; top: 204px; }
  .badge--efficient { left: 808px; top: 71px; }
  .badge--trustworthy { left: 808px; top: 204px; }

  .divider {
    position: absolute;
    height: 3px;
    width: 230px;
    background: linear-gradient(90deg, transparent, var(--rule) 20%, var(--rule) 80%, transparent);
  }
  .divider--l1 { left: 118px; top: 182px; }
  .divider--l2 { left: 118px; top: 318px; }
  .divider--r1 { left: 838px; top: 182px; }
  .divider--r2 { left: 838px; top: 318px; }

  .emblem { position: absolute; left: 434px; top: 40px; width: 332px; height: 332px; }

  .sun { position: absolute; border-radius: 50%; background: radial-gradient(circle, var(--white) 0 38%, var(--rose) 40% 100%); opacity: .9; }

  .wordmark {
    position: absolute;
    left: 240px; top: 378px; width: 730px;
    text-align: center;
    font-weight: 700;
    font-size: 80px;
    line-height: 1;
    letter-spacing: 2px;
    color: var(--magenta);
    white-space: nowrap;
  }
  .wordmark-rule { position: absolute; left: 240px; top: 468px; width: 730px; height: 10px; }

  .tagline {
    position: absolute;
    left: 240px; top: 500px; width: 730px;
    text-align: center;
    font-weight: 700;
    font-size: 32px;
    letter-spacing: 1.5px;
    color: var(--rose);
    white-space: nowrap;
  }
  .about {
    position: absolute;
    left: 228px; top: 546px; width: 370px;
    text-align: center;
    font-weight: 800;
    font-size: 13.5px;
    line-height: 1.25;
    color: var(--wine);
    text-transform: uppercase;
  }

  .social {
    position: absolute;
    top: 540px;
    width: 130px;
    display: flex; flex-direction: column; align-items: center;
  }
  .social__mark {
    width: 86px; height: 86px;
    border-radius: 50%;
    background: var(--magenta);
    display: flex; align-items: center; justify-content: center;
    color: var(--white);
    font-weight: 700;
    font-size: 17px;
  }
  .social__handle {
    margin-top: 5px;
    font-weight: 700;
    font-size: 11px;
    color: var(--wine);
    white-space: nowrap;
  }
  .social--chirper { left: 568px; }
  .social--facely { left: 698px; }
  .social--linkup { left: 838px; }

  .contact {
    position: absolute;
    left: 200px; top: 656px; width: 810px;
    display: flex; justify-content: center; gap: 14px;
    font-style: normal;
    font-weight: 700;
    font-size: 15px;
    color: var(--magenta);
    white-space: nowrap;
  }
  .contact__name { color: var(--wine); font-weight: 800; }
  .contact__sep { color: var(--rose-pale); }
</style>
</head>
<body>
<main class="card">

  <svg class="curtain curtain--left" viewBox="0 0 90 687" aria-hidden="true">
    <path d="M0 0 H62 Q40 200 34 360 Q30 540 48 687 H0 Z" fill="var(--rose-soft)"/>
    <path d="M0 0 H38 Q22 220 18 360 Q16 540 26 687 H0 Z" fill="var(--rose)"/>
    <path d="M-20 250 A68 68 0 0 1 -20 380" fill="none" stroke="var(--rose-soft)" stroke-width="14" transform="translate(60 0)"/>
  </svg>
  <svg class="curtain curtain--right" viewBox="0 0 90 687" aria-hidden="true">
    <path d="M90 0 H28 Q50 200 56 360 Q60 540 42 687 H90 Z" fill="var(--rose-soft)"/>
    <path d="M90 0 H52 Q68 220 72 360 Q74 540 64 687 H90 Z" fill="var(--rose)"/>
    <path d="M110 250 A68 68 0 0 0 110 380" fill="none" stroke="var(--rose-soft)" stroke-width="14" transform="translate(-60 0)"/>
  </svg>

  <div class="badge badge--quality">
    <svg viewBox="0 0 309 82" aria-hidden="true">
      <rect x="34" y="14" width="241" height="68" rx="9" fill="var(--rose-pale)"/>
      <rect x="34" y="7" width="241" height="68" rx="9" fill="var(--rose-soft)"/>
      <polygon points="0,14 34,14 34,54 0,54 16,34" fill="var(--rose)"/>
      <polygon points="309,14 275,14 275,54 309,54 293,34" fill="var(--rose)"/>
      <rect x="34" y="0" width="241" height="68" rx="9" fill="var(--rose)"/>
    </svg>
    <span class="badge__label">- HIGH QUALITY -</span>
  </div>
  <div class="badge badge--professional">
    <svg viewBox="0 0 309 82" aria-hidden="true">
      <rect x="34" y="14" width="241" height="68" rx="9" fill="var(--rose-pale)"/>
      <rect x="34" y="7" width="241" height="68" rx="9" fill="var(--rose-soft)"/>
      <polygon points="0,14 34,14 34,54 0,54 16,34" fill="var(--rose)"/>
      <polygon points="309,14 275,14 275,54 309,54 293,34" fill="var(--rose)"/>
      <rect x="34" y="0" width="241" height="68" rx="9" fill="var(--rose)"/>
    </svg>
    <span class="badge__label">- PROFESSIONAL -</span>
  </div>
  <div class="badge badge--efficient">
    <svg viewBox="0 0 309 82" aria-hidden="true">
      <rect x="34" y="14" width="241" height="68" rx="9" fill="var(--rose-pale)"/>
      <rect x="34" y="7" width="241" height="68" rx="9" fill="var(--rose-soft)"/>
      <polygon points="0,14 34,14 34,54 0,54 16,34" fill="var(--rose)"/>
      <polygon points="309,14 275,14 275,54 309,54 293,34" fill="var(--rose)"/>
      <rect x="34" y="0" width="241" height="68" rx="9" fill="var(--rose)"/>
    </svg>
    <span class="badge__label">- EFFICIENT -</span>
  </div>
  <div class="badge badge--trustworthy">
    <svg viewBox="0 0 309 82" aria-hidden="true">
      <rect x="34" y="14" width="241" height="68" rx="9" fill="var(--rose-pale)"/>
      <rect x="34" y="7" width="241" height="68" rx="9" fill="var(--rose-soft)"/>
      <polygon points="0,14 34,14 34,54 0,54 16,34" fill="var(--rose)"/>
      <polygon points="309,14 275,14 275,54 309,54 293,34" fill="var(--rose)"/>
      <rect x="34" y="0" width="241" height="68" rx="9" fill="var(--rose)"/>
    </svg>
    <span class="badge__label">- TRUSTWORTHY -</span>
  </div>

  <div class="divider divider--l1"></div>
  <div class="divider divider--l2"></div>
  <div class="divider divider--r1"></div>
  <div class="divider divider--r2"></div>

  <svg class="emblem" viewBox="0 0 332 332">
    <circle cx="166" cy="166" r="166" fill="var(--ring)"/>
    <circle cx="166" cy="166" r="146" fill="var(--white)"/>
    <circle cx="166" cy="166" r="140" fill="none" stroke="var(--rose)" stroke-width="10"/>
    <circle cx="166" cy="166" r="123" fill="var(--magenta)" role="img" aria-label="Mascot illustration: a cheerful masked office hero standing hands on hips"/>
  </svg>

  <div class="sun" style="left:92px;top:420px;width:76px;height:76px" role="img" aria-label="Decorative sunburst"></div>
  <div class="sun" style="left:140px;top:510px;width:62px;height:62px" role="img" aria-label="Decorative sunburst"></div>
  <div class="sun" style="left:102px;top:566px;width:44px;height:44px" role="img" aria-label="Decorative sunburst"></div>
  <div class="sun" style="left:1026px;top:420px;width:76px;height:76px" role="img" aria-label="Decorative sunburst"></div>
  <div class="sun" style="left:996px;top:500px;width:62px;height:62px" role="img" aria-label="Decorative sunburst"></div>
  <div class="sun" style="left:1056px;top:566px;width:44px;height:44px" role="img" aria-label="Decorative sunburst"></div>

  <h1 class="wordmark">OFFICE FALCON</h1>
  <svg class="wordmark-rule" viewBox="0 0 730 10" aria-hidden="true">
    <g fill="var(--magenta)">
      <rect x="0" y="0" width="16" height="10"/><rect x="30" y="0" width="16" height="10"/>
      <rect x="60" y="0" width="16" height="10"/><rect x="90" y="0" width="16" height="10"/>
      <rect x="120" y="0" width="16" height="10"/><rect x="150" y="0" width="16" height="10"/>
      <rect x="180" y="0" width="16" height="10"/><rect x="210" y="0" width="16" height="10"/>
      <rect x="240" y="0" width="16" height="10"/><rect x="270" y="0" width="16" height="10"/>
      <rect x="300" y="0" width="430" height="10"/>
    </g>
  </svg>

  <p class="tagline">CONTRACT ADMINISTRATIVE SERVICES</p>
  <p class="about">We provide high value administrative<br>services to small businesses/offices.<br>We are professional, efficient,<br>but also have fun and energetic<br>personalities.</p>

  <div class="social social--chirper">
    <span class="social__mark">Chirper</span>
    <span class="social__handle">@OFalconOlive</span>
  </div>
  <div class="social social--facely">
    <span class="social__mark">Facely</span>
    <span class="social__handle">OfficeFalconCanada</span>
  </div>
  <div class="social social--linkup">
    <span class="social__mark">Linkup</span>
    <span class="social__handle">OliveParkerOfficeFalcon</span>
  </div>

  <address class="contact">
    <span class="contact__name">Olive Parker</span>
    <span class="contact__sep">|</span>
    <span>Olive@OfficeFalcon.ca</span>
    <span class="contact__sep">|</span>
    <span>604-319-4870</span>
    <span class="contact__sep">|</span>
    <span>OfficeFalcon.ca</span>
  </address>

</main>
</body>
</html>
```